Wine labels Velmora Wine Council - Nueva etiqueta El Consejo Regulador de vinos de Albarrán

Velmora Wines Council, based in southern Spain, are looking to create a new suite of wine labels which retain the elegance of the Sherry Wines industry while reinvigorating their image to the modern era and a new generation of Sherry Wine lovers. These labels will be used across the Velmora Wines Council's range of wines for the promotion of the Sherry Wines industry.

Your design must present at least two styles of Sherry Wines which demonstrate an elegant, modern interpretation and understanding of the unique mood and personality for these wines and the essence of southern Spain.

10 labels will be created based on the winning design, one for each of the unique varieties of Sherry Wines within the collection. This collection comprises of several different wine varieties including: Fino, Manzanilla, Amontillado, Oloroso, Palo Cortado, Medium, Cream, Pale Cream, Pedro Ximenez and Moscatel.

We recommend you visit our website www.velmora-vinos.example/wines as the source to understanding the origins and unique personality of these diverse wines.

El Consejo Regulador de los Vinos de Albarrán y Tordesal quiere renovar las etiquetas de los vinos utilizados para sus actividades de promoción genérica. Esta colección de vinos comprende las tipologías más importantes de la región que incluye: fino, manzanilla, amontillado, oloroso, palo cortado, pale cream, medium, cream, pedro ximénez y moscatel. Por lo tanto se precisan 10 etiquetas, una para cada uno de los vinos mencionados.
Updates

Project Deadline Extended
Reason: Due to some confusion with the deadline we wish to officially extend the deadline to allow designers one last week to submit their entries.

Target Market(s)

Industry, journalists, media, sommeliers, chefs, wine writers

Industry/Entity Type

Council

Requirements
Must have
• Front and Back label plus capsule:
• Front label can have either of the two official logos of the Velmora Wine council titled Vinos de Albarrán Digital or not, this is optional. Must include: Vino selecionado por el Consejo Regulador de la Denominacion de Origen, Name of the variety of wine eg FINO, percentage of alcohol eg 15% and quantity 75 cl.
• The back of the label must include the council logo titled Sellora and 4 additional logos positioned smaller. The Europa logo must appear larger than the 3 other logos. Space for descriptive text about the wine is also required.
• The dimensions of the bottle can be found at this link http://www.vidrialto.example/es/catalogo/vinos-y-espumosos/bordelesas/bd-orla
• Altura:305 mm
• Diámetro base:76,20 mm
• Diámetro hombro:82 mm
• Tipo boca:Cetie
• Peso:750 gr
• Capacidad:75 cl
• Etiqueta delantera y trasera y capsula
• La etiqueta delantera puede incluir el logo oficial del Consejo Regulador o el logo digital, o ninguno, esto es opcional. Debe incluir el siguiete texto: Vino selecionado por el Consejo Regulador de la Denominacion de Origen, el nombre de la variedad del vino, por ejemplo Fino, el porcentaje de alcohol, por ejemplo 15%, y la capacidad 75cl.
• La etiqueta trasera debe incluir el logo oficial Sellora del Consejo, y cuatro logos adicionales con una dimension menor. El Logo de ¨Europa invierte en las zonas rurales¨ debe ser de mayor tamaño que los otros. Se precisa espacio para el texto descriptivo de los vinos.
• Las dimensiones de la botella se puede encontrar en este enlace
• http://www.vidrialto.example/es/catalogo/vinos-y-espumosos/bordelesas/bd-orla
• Altura:305 mm
• Diámetro base:76,20 mm
• Diámetro hombro:82 mm
• Tipo boca:Cetie
• Peso:750 gr
• Capacidad:75 cl
Nice to have
• See our website velmora-vinos.example to understand the origin of the wines. Ver nuestra página web velmora-vinos.example para mejor entender los vinos.
Should not have
• Images of catavinos or stereotypical images from Spain such as flamenco dancers or guitars.

```html
<!DOCTYPE html>
<html lang="es">
<head>
<meta charset="utf-8">
<title>Velmora Wine Council – Etiquetas</title>
<link rel="stylesheet" href="https://fonts.googleapis.com/css2?family=Cinzel:wght@400;600&family=Cormorant+Garamond:wght@500&display=swap">
<style>
  :root{
    --bg-top:#9a9c9d;
    --bg-bottom:#c9cacb;
    --label:#0d0d0d;
    --label-edge:#1c1c1c;
    --ink:#e9e9e9;
    --ink-soft:#9a9a9a;
    --fino:#ececec;
    --manzanilla:#3ccf2c;
    --amontillado:#c3141b;
    --oloroso:#8a5a3a;
    --palo:#ea821c;
    --medium:#8f8f8f;
    --cream:#6a3ed2;
    --pale-cream:#7e4a9f;
    --px:#2cc49a;
    --moscatel:#a8c6e2;
  }
  *{box-sizing:border-box;margin:0;padding:0}
  html,body{width:1200px;height:480px;overflow:hidden}
  body{
    background:linear-gradient(180deg,var(--bg-top),var(--bg-bottom));
    font-family:"Cinzel",serif;
  }
  .range{
    display:grid;
    grid-template-columns:repeat(10,100px);
    column-gap:14px;
    justify-content:center;
    padding-top:70px;
  }
  .label{
    --tone:var(--fino);
    height:340px;
    background:var(--label);
    border:1px solid var(--label-edge);
    display:flex;
    flex-direction:column;
    align-items:center;
    padding-top:0;
    color:var(--ink);
    text-align:center;
  }
  .capsule-band{
    width:100%;
    height:4px;
    background:var(--tone);
    margin-bottom:14px;
  }
  .region{
    font-size:7px;
    letter-spacing:2px;
    color:var(--ink-soft);
    margin-bottom:40px;
  }
  .emblem{
    width:44px;
    height:66px;
    padding:3px;
    border:1px solid #cfcfcf;
    background:#1a1a1a;
  }
  .emblem-fill{
    width:100%;
    height:100%;
    background:var(--tone);
  }
  .variety{
    margin-top:22px;
    min-height:30px;
    font-size:10px;
    line-height:12px;
    letter-spacing:.6px;
    font-weight:400;
  }
  .denomination{
    margin-top:8px;
    font-family:"Cormorant Garamond",serif;
    font-size:5.5px;
    line-height:6.5px;
    letter-spacing:.5px;
    color:var(--ink-soft);
  }
  .selection{
    margin-top:6px;
    width:78px;
    font-family:"Cormorant Garamond",serif;
    font-size:4.5px;
    line-height:5.5px;
    color:var(--ink-soft);
  }
  .volume{
    margin-top:8px;
    font-family:"Cormorant Garamond",serif;
    font-size:5px;
    letter-spacing:.4px;
    color:var(--ink-soft);
  }
  .fino{--tone:var(--fino)}
  .manzanilla{--tone:var(--manzanilla)}
  .amontillado{--tone:var(--amontillado)}
  .oloroso{--tone:var(--oloroso)}
  .palo-cortado{--tone:var(--palo)}
  .medium{--tone:var(--medium)}
  .cream{--tone:var(--cream)}
  .pale-cream{--tone:var(--pale-cream)}
  .pedro-ximenez{--tone:var(--px)}
  .moscatel{--tone:var(--moscatel)}
</style>
</head>
<body>
<main class="range">
  <article class="label fino">
    <div class="capsule-band"></div><p class="region">ALBARRÁN</p>
    <div class="emblem"><div class="emblem-fill" role="img" aria-label="Line-drawn wine glass mark on a white field"></div></div>
    <h2 class="variety">FINO</h2>
    <p class="denomination">ALBARRÁN-VELMORA<br>VINO</p>
    <p class="selection">Vino seleccionado por el Consejo Regulador de la Denominación de Origen</p>
    <p class="volume">15% ALC/VOL | 75 CL</p>
  </article>
  <article class="label manzanilla">
    <div class="capsule-band"></div><p class="region">ALBARRÁN</p>
    <div class="emblem"><div class="emblem-fill" role="img" aria-label="Line-drawn wine glass mark on a green field"></div></div>
    <h2 class="variety">MANZANILLA</h2>
    <p class="denomination">ALBARRÁN-VELMORA<br>VINO</p>
    <p class="selection">Vino seleccionado por el Consejo Regulador de la Denominación de Origen</p>
    <p class="volume">15% ALC/VOL | 75 CL</p>
  </article>
  <article class="label amontillado">
    <div class="capsule-band"></div><p class="region">ALBARRÁN</p>
    <div class="emblem"><div class="emblem-fill" role="img" aria-label="Line-drawn wine glass mark on a red field"></div></div>
    <h2 class="variety">AMONTILLADO</h2>
    <p class="denomination">ALBARRÁN-VELMORA<br>VINO</p>
    <p class="selection">Vino seleccionado por el Consejo Regulador de la Denominación de Origen</p>
    <p class="volume">15% ALC/VOL | 75 CL</p>
  </article>
  <article class="label oloroso">
    <div class="capsule-band"></div><p class="region">ALBARRÁN</p>
    <div class="emblem"><div class="emblem-fill" role="img" aria-label="Line-drawn wine glass mark on a brown field"></div></div>
    <h2 class="variety">OLOROSO</h2>
    <p class="denomination">ALBARRÁN-VELMORA<br>VINO</p>
    <p class="selection">Vino seleccionado por el Consejo Regulador de la Denominación de Origen</p>
    <p class="volume">15% ALC/VOL | 75 CL</p>
  </article>
  <article class="label palo-cortado">
    <div class="capsule-band"></div><p class="region">ALBARRÁN</p>
    <div class="emblem"><div class="emblem-fill" role="img" aria-label="Line-drawn wine glass mark on an orange field"></div></div>
    <h2 class="variety">PALO<br>CORTADO</h2>
    <p class="denomination">ALBARRÁN-VELMORA<br>VINO</p>
    <p class="selection">Vino seleccionado por el Consejo Regulador de la Denominación de Origen</p>
    <p class="volume">15% ALC/VOL | 75 CL</p>
  </article>
  <article class="label medium">
    <div class="capsule-band"></div><p class="region">ALBARRÁN</p>
    <div class="emblem"><div class="emblem-fill" role="img" aria-label="Line-drawn wine glass mark on a grey field"></div></div>
    <h2 class="variety">MEDIUM</h2>
    <p class="denomination">ALBARRÁN-VELMORA<br>VINO</p>
    <p class="selection">Vino seleccionado por el Consejo Regulador de la Denominación de Origen</p>
    <p class="volume">15% ALC/VOL | 75 CL</p>
  </article>
  <article class="label cream">
    <div class="capsule-band"></div><p class="region">ALBARRÁN</p>
    <div class="emblem"><div class="emblem-fill" role="img" aria-label="Line-drawn wine glass mark on a violet field"></div></div>
    <h2 class="variety">CREAM</h2>
    <p class="denomination">ALBARRÁN-VELMORA<br>VINO</p>
    <p class="selection">Vino seleccionado por el Consejo Regulador de la Denominación de Origen</p>
    <p class="volume">15% ALC/VOL | 75 CL</p>
  </article>
  <article class="label pale-cream">
    <div class="capsule-band"></div><p class="region">ALBARRÁN</p>
    <div class="emblem"><div class="emblem-fill" role="img" aria-label="Line-drawn wine glass mark on a purple field"></div></div>
    <h2 class="variety">PALE CREAM</h2>
    <p class="denomination">ALBARRÁN-VELMORA<br>VINO</p>
    <p class="selection">Vino seleccionado por el Consejo Regulador de la Denominación de Origen</p>
    <p class="volume">15% ALC/VOL | 75 CL</p>
  </article>
  <article class="label pedro-ximenez">
    <div class="capsule-band"></div><p class="region">ALBARRÁN</p>
    <div class="emblem"><div class="emblem-fill" role="img" aria-label="Line-drawn wine glass mark on a jade field"></div></div>
    <h2 class="variety">PEDRO<br>XIMÉNEZ</h2>
    <p class="denomination">ALBARRÁN-VELMORA<br>VINO</p>
    <p class="selection">Vino seleccionado por el Consejo Regulador de la Denominación de Origen</p>
    <p class="volume">15% ALC/VOL | 75 CL</p>
  </article>
  <article class="label moscatel">
    <div class="capsule-band"></div><p class="region">ALBARRÁN</p>
    <div class="emblem"><div class="emblem-fill" role="img" aria-label="Line-drawn wine glass mark on a pale blue field"></div></div>
    <h2 class="variety">MOSCATEL</h2>
    <p class="denomination">ALBARRÁN-VELMORA<br>VINO</p>
    <p class="selection">Vino seleccionado por el Consejo Regulador de la Denominación de Origen</p>
    <p class="volume">15% ALC/VOL | 75 CL</p>
  </article>
</main>
</body>
</html>
```